The Silver Creek subtitle: Sailing Under a Lantern of Belief

I need a cover for my new book. This book will help readers to develop a healthy relationship with their money and teach them skills to manage, invest, and plan for the future. It is intended for a Christian audience, so it will include references to stewardship and show them how to give more effectively. Leaving legacies of financial resources and legacies of love, encouragement, and hope are covered. Also covered (based on the author's 30 plus years of experience as an estate planning attorney, are estate planning techniques and techniques to help readers be prepared for possible disabilities and illnesses.
Updates

I've gotten some really nice designs and I actually like all of them (some more than others).All of them are what I would call professional mode, which I indicated on the order. However, after reflecting, I would like to see something a little more on the fun side since money is a heavy topic for many.Maybe a funky font and a cartoon river with money floating on it (along with whatever else you can think of).Many thanks!Mara Tolland Added Saturday, May 28, 2016

Target Market(s)

Church members - middle to upper income levels

Font styles to use
Serif
Other font styles liked:
• see image below

Requirements
Must have
• knock out cover - very attractive
Nice to have
• the book can be used by groups for short term studies -
• could say this , but I'm not sure how it would look

```html
<!DOCTYPE html>
<html lang="en">
<head>
<meta charset="utf-8">
<title>The Silver Creek — Book Cover Wrap</title>
<link rel="stylesheet" href="https://fonts.googleapis.com/css2?family=Cinzel:wght@400;500&family=Crimson+Text:wght@400&display=swap">
<style>
  :root {
    --backdrop: #4b4b4b;
    --paper: #eee9e0;
    --paper-light: #f7f4ee;
    --gold: #a9894f;
    --gold-deep: #8c6f3a;
    --ink: #3c3a36;
    --photo-grey: #9a9a9a;
    --coin-tone: #d4b06a;
  }
  * { margin: 0; padding: 0; box-sizing: border-box; }
  html, body {
    width: 1200px; height: 800px; overflow: hidden;
    background: var(--backdrop);
  }
  .cover-wrap {
    position: absolute; left: 105px; top: 50px;
    width: 990px; height: 700px;
    display: flex;
    background: var(--paper);
  }
  .back-cover, .front-cover {
    position: relative; width: 470px; height: 100%;
    background: radial-gradient(ellipse at 50% 40%, var(--paper-light) 0%, var(--paper) 70%);
  }
  .spine {
    position: relative; width: 50px; height: 100%;
    background: var(--paper);
    border-left: 1px solid rgba(0,0,0,0.06);
    border-right: 1px solid rgba(0,0,0,0.06);
  }
  .title-block {
    font-family: "Cinzel", serif; color: var(--gold);
    text-align: center; line-height: 0.95; font-weight: 400;
  }
  .title-block .title-article { display: block; }
  .title-block .title-word { display: block; letter-spacing: 0.03em; }

  /* Back cover */
  .back-cover .title-block { padding-top: 62px; }
  .back-cover .title-article { font-size: 18px; margin-bottom: 4px; }
  .back-cover .title-word { font-size: 36px; }
  .blurb {
    font-family: "Crimson Text", serif; color: var(--ink);
    font-size: 12.5px; line-height: 1.45; text-align: justify;
    margin: 26px 40px 0 40px;
  }
  .divider-dots {
    display: flex; justify-content: center; gap: 7px; margin: 16px 0 18px;
  }
  .divider-dots span {
    width: 4px; height: 4px; border-radius: 50%; background: var(--ink);
  }
  .author-bio { display: flex; gap: 14px; margin: 0 40px; }
  .author-photo {
    flex: 0 0 60px; height: 86px; background: var(--photo-grey); margin-top: 4px;
  }
  .author-bio p {
    font-family: "Crimson Text", serif; color: var(--ink);
    font-size: 11.5px; line-height: 1.45; text-align: justify;
  }

  /* Spine */
  .spine-text {
    position: absolute; left: 50%; top: 40px;
    transform: translateX(-50%);
    writing-mode: vertical-rl;
    font-family: "Cinzel", serif; color: var(--gold);
    display: flex; align-items: center; gap: 40px;
    white-space: nowrap;
  }
  .spine-title { font-size: 24px; letter-spacing: 0.06em; }
  .spine-author { font-size: 18px; letter-spacing: 0.2em; }

  /* Front cover */
  .cover-photo {
    position: absolute; left: 40px; top: 24px; width: 400px; height: 236px;
    background: radial-gradient(ellipse at 50% 50%, var(--coin-tone) 0%, rgba(212,176,106,0.45) 45%, rgba(238,233,224,0) 75%);
  }
  .front-cover .title-block { position: absolute; left: 0; right: 0; top: 282px; }
  .front-cover .title-article { font-size: 34px; margin-bottom: 2px; }
  .front-cover .title-word { font-size: 64px; }
  .subtitle {
    position: absolute; left: 0; right: 0; top: 488px;
    font-family: "Cinzel", serif; color: var(--gold-deep);
    font-size: 16px; line-height: 1.3; text-align: center; letter-spacing: 0.02em;
  }
  .author-name {
    position: absolute; left: 0; right: 0; top: 600px;
    font-family: "Cinzel", serif; color: var(--gold-deep);
    font-size: 24px; text-align: center; letter-spacing: 0.22em;
  }
</style>
</head>
<body>
  <main class="cover-wrap">
    <section class="back-cover">
      <h2 class="title-block">
        <span class="title-article">The</span>
        <span class="title-word">Silver</span>
        <span class="title-word">Creek</span>
      </h2>
      <p class="blurb">Money can feel like a heavy current, yet it was meant to carry blessing. This book helps readers build a calm and healthy relationship with their money, learning to budget, invest and plan ahead with wisdom. Rooted in stewardship, it shows how to give with purpose and joy. Drawing on decades of estate planning practice, it explains wills, trusts and care for times of illness, so families are ready. Above all, it invites readers to leave a legacy of resources, love, encouragement and lasting hope.</p>
      <div class="divider-dots"><span></span><span></span><span></span><span></span><span></span><span></span></div>
      <div class="author-bio">
        <div class="author-photo" role="img" aria-label="Author portrait placeholder"></div>
        <p>Mara Tolland has served families as an estate planning attorney for more than thirty years. She teaches church groups how to manage money faithfully, give generously and prepare for the future. She lives near a quiet creek with her family and still believes every coin can become a seed of hope.</p>
      </div>
    </section>

    <section class="spine">
      <div class="spine-text">
        <span class="spine-title">The Silver Creek</span>
        <span class="spine-author">Mara Tolland</span>
      </div>
    </section>

    <section class="front-cover">
      <div class="cover-photo" role="img" aria-label="Photograph of a stream of gold coins flowing down from the top right corner"></div>
      <h1 class="title-block">
        <span class="title-article">The</span>
        <span class="title-word">Silver</span>
        <span class="title-word">Creek</span>
      </h1>
      <p class="subtitle">Sailing Under a Lantern<br>of Belief</p>
      <p class="author-name">Mara Tolland</p>
    </section>
  </main>
</body>
</html>
```